Vendor Managed Inventory Talking points/Customer hand out

Looking for a single page flyer/Customer handout to be a sell sheet for our Vendor managed Inventory programs
Title: VMI benefits
Risk management:
Identification of Items and values that are sole sourced
Ongoing plans to reduce exposure to sole sourced items
Schedule planning to eliminate freight and outages
Reducing the hidden costs of forecasting errors
(Note; with us managing the point of use we can more accurately forecast)
Managing ever shortening of product lifecycles, minimizing obsolescence
Zero Inventory Exposure:
Minimized or Zero inventory on commodity items
Greatly reducing the Weighted Cost of Capital (WACC)
Reduced WACC can help in calculating Hurdle Rates
True point of use billing:
Allows for better tracking and allocation of expenses from a job-job basis
Custom labeling:
Including things like customer part numbers, exp dates, internal hazmat codes
Insures accurate processes with current materials
Helps to meet 5S requirements
Required for certain audits
Lot tracking/Shelf life:
Active assistance in managing Date Codes/Lot Tracking
Shortened shelf life products identified and managed
Plain statement of expiration dates on products. Calculations are not required
Taken as a whole we can help calculate TRUE management and landed costs of products. Focusing only on the price of items is like looking at just the exposed part of an iceberg. Let RT7K help you to see what's underneath.
I have attached some other brochures and flyers for style reference
more info on our website too. www.rt7k-example.com
Target Market(s)
Electronics manufacturers
Industry/Entity Type
Electronics
Look and feel

```html
<!DOCTYPE html>
<html lang="en">
<head>
<meta charset="utf-8">
<title>VMI Benefits – RT7K</title>
<link href="https://fonts.googleapis.com/css2?family=Oswald:wght@400;500;600&family=Open+Sans:wght@400;600&display=swap" rel="stylesheet">
<style>
:root{
  --blue:#0a6fc2;
  --blue-deep:#0657a3;
  --blue-light:#2b8fe0;
  --ink:#1b1b1b;
  --text:#4a4a4a;
  --grey-soft:#eeeeee;
  --white:#ffffff;
}
*{margin:0;padding:0;box-sizing:border-box}
html,body{width:1003px;height:1200px;overflow:hidden;background:#fff}
.flyer{position:relative;width:1003px;height:1200px;overflow:hidden;background:var(--white);font-family:"Open Sans",sans-serif;color:var(--text)}
.hero-photo{position:absolute;left:0;top:0;width:1003px;height:480px;background:linear-gradient(135deg,#2a2c30 0%,#55585e 40%,#a9adb3 70%,#dcdfe3 100%)}
.hero-shapes{position:absolute;left:0;top:0}
.brand{position:absolute;left:640px;top:24px;width:340px;text-align:center}
.brand-name{display:flex;align-items:center;justify-content:center;gap:14px;font-family:"Oswald",sans-serif;font-weight:600;font-size:72px;line-height:1;color:var(--blue)}
.brand-dot{width:24px;height:24px;border-radius:50%;background:var(--blue)}
.brand-line{margin-top:12px;font-family:"Oswald",sans-serif;font-weight:500;font-size:19px;letter-spacing:1px;line-height:1.2;text-transform:uppercase;color:var(--ink)}
.title-badge{position:absolute;left:730px;top:284px;width:240px;height:240px;border-radius:50%;background:radial-gradient(circle at 40% 35%,var(--blue-light),var(--blue-deep));border:5px solid #fff;box-shadow:0 4px 10px rgba(0,0,0,.3);display:flex;flex-direction:column;align-items:center;justify-content:center;font-family:"Oswald",sans-serif;font-weight:600;color:#fff;font-size:52px;line-height:1.08;text-align:center}
.section{position:absolute}
.section-head{display:flex;align-items:center;gap:20px;height:76px}
.icon{width:72px;height:72px;flex:none}
.section-title{font-family:"Oswald",sans-serif;font-weight:400;font-size:26px;color:var(--blue);text-transform:uppercase;letter-spacing:-.2px;white-space:nowrap}
.bullets{list-style:none;margin-top:10px;font-size:14px;line-height:19.5px}
.bullets li{padding-left:9px;text-indent:-9px}
.bullets li::before{content:"• ";font-size:10px}
.bullets .note{font-size:10.5px;line-height:15px;padding-left:0;text-indent:0}
.bullets .note::before{content:""}
.corner-swoosh{position:absolute;left:0;top:930px}
.summary{position:absolute;left:531px;top:946px;width:472px;height:164px;background:linear-gradient(180deg,var(--blue) 0%,var(--blue-deep) 100%);border-radius:10px 0 0 10px;box-shadow:0 3px 6px rgba(0,0,0,.25);padding:26px 26px 0 38px;color:#fff;font-size:15.5px;line-height:21px;text-align:justify}
.footer{position:absolute;left:0;top:1134px;width:1003px;height:66px;background:linear-gradient(90deg,#151515,#3b3b3b 50%,#151515);border-top:6px solid var(--blue);display:flex;align-items:center;padding:0 16px 0 40px;color:#fff;font-size:14px;font-weight:600;line-height:16px;white-space:nowrap}
.contact{display:flex;align-items:center;gap:12px}
.contact svg{width:30px;height:30px;flex:none}
.contact.address{width:228px}
.contact.phone{width:208px}
.contact.web{width:262px}
</style>
</head>
<body>
<main class="flyer">
  <div class="hero-photo" role="img" aria-label="Photo of a storage cabinet with rows of clear parts bins holding electronic components"></div>
  <svg class="hero-shapes" width="1003" height="540" viewBox="0 0 1003 540">
    <path d="M497 0 H1003 V235 C860 215 740 195 668 169 C600 140 540 80 497 0 Z" fill="#fff"/>
    <path d="M668 169 C740 195 860 215 1003 235 V258 C850 245 730 215 668 169 Z" fill="var(--blue)"/>
    <path d="M0 380 C250 440 520 478 760 468 C870 460 950 420 1003 385 V410 C950 445 860 485 760 492 C520 505 250 470 0 412 Z" fill="var(--blue)"/>
    <path d="M0 412 C250 470 520 505 760 492 C860 485 950 445 1003 410 V425 C950 465 860 505 760 512 C520 522 250 495 0 450 Z" fill="var(--ink)"/>
    <path d="M0 450 C250 495 520 522 760 512 C860 505 950 465 1003 425 V540 H0 Z" fill="#fff"/>
  </svg>

  <div class="brand">
    <div class="brand-name"><span class="brand-dot"></span>RT7K</div>
    <div class="brand-line">Ridgeline Technical Parts Services</div>
  </div>

  <div class="title-badge">VMI<br>BENEFITS</div>

  <svg class="corner-swoosh" width="420" height="210" viewBox="0 0 420 210">
    <path d="M0 0 C20 90 140 170 420 200 V210 H0 Z" fill="var(--grey-soft)"/>
  </svg>

  <section class="section" style="left:42px;top:542px;width:450px">
    <div class="section-head">
      <svg class="icon" viewBox="0 0 76 76"><circle cx="38" cy="38" r="36" fill="#e6e6e6"/><circle cx="38" cy="38" r="31" fill="var(--blue)"/><rect x="26" y="22" width="20" height="30" rx="2" fill="none" stroke="#fff" stroke-width="2.5"/><path d="M30 30h12M30 36h12M30 42h8" stroke="#fff" stroke-width="2"/><rect x="42" y="40" width="12" height="10" rx="1.5" fill="#fff"/><path d="M44.5 40v-3a3.5 3.5 0 0 1 7 0v3" fill="none" stroke="#fff" stroke-width="2"/></svg>
      <h2 class="section-title">Risk Management</h2>
    </div>
    <ul class="bullets">
      <li>Identification of Items and values that are sole sourced</li>
      <li>Ongoing plans to reduce exposure to sole sourced items</li>
      <li>Schedule planning to eliminate freight and outages</li>
      <li>Reducing the hidden costs of forecasting errors</li>
      <li class="note">(Note; with us managing the point of use we can more accurately forecast)</li>
      <li>Managing ever shortening of product lifecycles, minimizing obsolescence</li>
    </ul>
  </section>

  <section class="section" style="left:530px;top:542px;width:440px">
    <div class="section-head">
      <svg class="icon" viewBox="0 0 76 76"><circle cx="38" cy="38" r="36" fill="#e6e6e6"/><circle cx="38" cy="38" r="31" fill="var(--blue)"/><circle cx="33" cy="41" r="9" fill="none" stroke="#fff" stroke-width="5" stroke-dasharray="4 3"/><circle cx="33" cy="41" r="3" fill="#fff"/><circle cx="47" cy="28" r="5" fill="none" stroke="#fff" stroke-width="3" stroke-dasharray="3 2"/></svg>
      <h2 class="section-title">Custom Labeling</h2>
    </div>
    <ul class="bullets">
      <li>Including things like customer part numbers, exp dates, internal hazmat codes</li>
      <li>Insures accurate processes with current materials</li>
      <li>Helps to meet 5S requirements</li>
      <li>Required for certain audits</li>
    </ul>
  </section>

  <section class="section" style="left:42px;top:780px;width:450px">
    <div class="section-head">
      <svg class="icon" viewBox="0 0 76 76"><circle cx="38" cy="38" r="36" fill="#e6e6e6"/><circle cx="38" cy="38" r="31" fill="var(--blue)"/><text x="38" y="49" text-anchor="middle" font-family="Oswald,sans-serif" font-weight="600" font-size="32" fill="#fff">0</text></svg>
      <h2 class="section-title">Zero Inventory Exposure</h2>
    </div>
    <ul class="bullets">
      <li>Minimized or Zero inventory on commodity items</li>
      <li>Greatly reducing the Weighted Cost of Capital (WACC)</li>
      <li>Reduced WACC can help in calculating Hurdle Rates</li>
    </ul>
  </section>

  <section class="section" style="left:530px;top:762px;width:440px">
    <div class="section-head">
      <svg class="icon" viewBox="0 0 76 76"><circle cx="38" cy="38" r="36" fill="#e6e6e6"/><circle cx="38" cy="38" r="31" fill="var(--blue)"/><g fill="none" stroke="#fff" stroke-width="2"><rect x="33" y="22" width="10" height="8"/><rect x="22" y="44" width="9" height="8"/><rect x="34" y="44" width="9" height="8"/><rect x="46" y="44" width="9" height="8"/><path d="M38 30v7M26 44v-7h24v7M38 37v7"/></g></svg>
      <h2 class="section-title">Lot Tracking/Shelf Life</h2>
    </div>
    <ul class="bullets">
      <li>Active assistance in managing Date Codes/Lot Tracking</li>
      <li>Shortened shelf life products identified and managed</li>
      <li>Plain statement of expiration dates on products. Calculations are not required</li>
    </ul>
  </section>

  <section class="section" style="left:42px;top:936px;width:450px">
    <div class="section-head">
      <svg class="icon" viewBox="0 0 76 76"><circle cx="38" cy="38" r="36" fill="#e6e6e6"/><circle cx="38" cy="38" r="31" fill="var(--blue)"/><path d="M20 50V40M25 50V34M30 50V38" stroke="#fff" stroke-width="3"/><path d="M45 38V27a11 11 0 1 1-11 11Z" fill="#fff"/><path d="M47 25a11 11 0 0 1 11 11H47Z" fill="#fff"/></svg>
      <h2 class="section-title">True Point of Use Billing</h2>
    </div>
    <ul class="bullets">
      <li>Minimized or Zero inventory on commodity items</li>
      <li>Greatly reducing the Weighted Cost of Capital (WACC)</li>
      <li>Reduced WACC can help in calculating Hurdle Rates</li>
    </ul>
  </section>

  <aside class="summary">Taken as a whole we can help calculate TRUE management and landed costs of products. Focusing only on the price of items is like looking at just the exposed part of an iceberg. Let RT7K help you to see what’s underneath.</aside>

  <footer class="footer">
    <div class="contact address">
      <svg viewBox="0 0 30 30"><circle cx="15" cy="15" r="14" fill="var(--blue)"/><path d="M8 15l7-6 7 6M10 14v7h10v-7" fill="none" stroke="#fff" stroke-width="2"/></svg>
      <span>418 Alder Lane<br>Millbrook, PA 17000</span>
    </div>
    <div class="contact phone">
      <svg viewBox="0 0 30 30"><circle cx="15" cy="15" r="14" fill="var(--blue)"/><path d="M10 8c-2 2-1 6 3 10s8 5 10 3l-3-3-2 1c-2-1-4-3-5-5l1-2Z" fill="#fff"/></svg>
      <span>800.555.0142</span>
    </div>
    <div class="contact web">
      <svg viewBox="0 0 30 30"><circle cx="15" cy="15" r="14" fill="var(--blue)"/><g fill="none" stroke="#fff" stroke-width="1.5"><circle cx="15" cy="15" r="7"/><ellipse cx="15" cy="15" rx="3" ry="7"/><path d="M8 15h14"/></g></svg>
      <span>www.rt7k-example.com</span>
    </div>
    <div class="contact email">
      <svg viewBox="0 0 30 30"><circle cx="15" cy="15" r="14" fill="var(--blue)"/><rect x="8" y="10" width="14" height="10" fill="none" stroke="#fff" stroke-width="1.8"/><path d="M8 10l7 6 7-6" fill="none" stroke="#fff" stroke-width="1.8"/></svg>
      <span>sales@rt7k-example.com</span>
    </div>
  </footer>
</main>
</body>
</html>
```